Vel Corvanta Logo Design

We need a business card design for Las Vegas based company called "Vel Corvanta" (http://www.velcorvanta-example.com). Vel Corvanta prides itself in providing in-depth knowledge that is based on real-world experience in the field of wireless telecommunications. Our practice covers strategy, marketing, and business development across the entire telecom value chain – from consumer to enterprise, content to applications, and mobile devices to wireless infrastructure. Our expertise is in the fields of wireless telecommunications, network optimization, specializing in CDMA, UMTS, WiMAX and LTE solutions.
The logo attached could be reused for the business card, but would prefer a new innovative logo as well. The final design should project cutting edge wireless technologies. The design should also communicate a modern business that has expertise and is focused on R&D.
Updates

Team,

  Forgot to mention this.  While Vel Corvanta is focused in wireless technologies, the word 'Vel' comes from Hindi language and means harmonious music

Project Deadline Extended
Reason: Extending deadline to allow for the designer to complete final changes. Thank you all for submitting the designs so far. Thanks, Toren.

Industry/Entity Type

Business

Logo Text

Vel Corvanta

```html
<!DOCTYPE html>
<html lang="en">
<head>
<meta charset="utf-8">
<title>Vel Corvanta – Business Card</title>
<link href="https://fonts.googleapis.com/css2?family=Michroma&family=Arimo:wght@700&display=swap" rel="stylesheet">
<style>
  :root {
    --board: #d3d4d6;
    --card: #ffffff;
    --brand-blue: #1a8fd0;
    --band-light: #4fb0e2;
    --band-dark: #1c7cc2;
    --band-edge: #1463a6;
    --ink: #5b5f63;
    --ink-dark: #4a4d50;
    --label: #2b2b2b;
  }
  * { box-sizing: border-box; margin: 0; padding: 0; }
  html, body { width: 935px; height: 1200px; overflow: hidden; }
  body {
    background: var(--board);
    font-family: "Michroma", sans-serif;
    position: relative;
  }
  .side-label {
    position: absolute;
    left: 44px;
    font-family: "Arimo", sans-serif;
    font-weight: 700;
    font-size: 21px;
    color: var(--label);
  }
  .side-label.front { top: 22px; }
  .side-label.back { top: 603px; }

  .card {
    position: absolute;
    background: var(--card);
    box-shadow: 0 4px 14px rgba(0,0,0,0.35);
    overflow: hidden;
  }
  .card-front { left: 42px; top: 62px; width: 852px; height: 499px; }
  .card-back { left: 42px; top: 654px; width: 857px; height: 500px; }

  .side-band {
    position: absolute; left: 0; top: 0; bottom: 0; width: 148px;
    background: linear-gradient(180deg, var(--band-dark) 0%, var(--band-light) 45%, var(--band-dark) 100%);
  }
  .side-band::after {
    content: ""; position: absolute; right: -5px; top: 0; bottom: 0; width: 5px;
    background: var(--band-edge);
  }

  .holder-name {
    position: absolute; left: 184px; top: 146px;
    font-size: 23px; color: var(--brand-blue); letter-spacing: 0.5px;
  }
  .holder-title {
    position: absolute; left: 184px; top: 190px;
    font-size: 17px; color: var(--ink);
  }

  .brand { position: absolute; inset: 0; }
  .brand-mark { position: absolute; }
  .brand-name {
    position: absolute; white-space: nowrap;
    font-size: 25px; line-height: 1; color: var(--ink); letter-spacing: 0.3px;
  }
  .card-front .brand-mark { left: 610px; top: 52px; }
  .card-front .brand-name { left: 520px; top: 184px; }
  .card-back .brand-mark { left: 211px; top: 156px; }
  .card-back .brand-name { left: 97px; top: 304px; }

  .contact-block {
    position: absolute; right: 51px; text-align: right;
    font-size: 19px; color: var(--ink); line-height: 36px;
  }
  .contact-block.address { top: 286px; }
  .contact-block.phone { top: 394px; }

  .online {
    position: absolute; left: 0; right: 0; text-align: center;
    transform: translateX(-28px);
    font-size: 17px; color: var(--ink-dark); line-height: 36px;
  }
  .online.email { top: 390px; }
  .online.web { top: 428px; }
</style>
</head>
<body>
  <div class="side-label front">Front</div>
  <section class="card card-front">
    <div class="side-band"></div>
    <div class="holder-name">YOUR NAME</div>
    <div class="holder-title">C.E.O</div>
    <div class="brand">
      <svg class="brand-mark" width="108" height="108" viewBox="0 0 108 108" aria-hidden="true">
        <circle cx="54" cy="54" r="53" fill="var(--brand-blue)"/>
      </svg>
      <div class="brand-name">VEL CORVANTA</div>
    </div>
    <div class="contact-block address">Marlow Crest Road,<br>PO Box 51820</div>
    <div class="contact-block phone">PH:+2140 555 0192</div>
  </section>

  <div class="side-label back">Back</div>
  <section class="card card-back">
    <div class="brand">
      <svg class="brand-mark" width="108" height="108" viewBox="0 0 108 108" aria-hidden="true">
        <circle cx="54" cy="54" r="53" fill="var(--brand-blue)"/>
      </svg>
      <div class="brand-name">VEL CORVANTA</div>
    </div>
    <div class="online email">E-mail:info@velcorvanta-example.com</div>
    <div class="online web">www.velcorvanta-example.com</div>
  </section>
</body>
</html>
```